Fabric Softener

We need fabric softener. Bottle picture attached for reference. Color of bottle can be proposed as well. Normally bottle is pink and blue color

Logo is also attached that shall be used.
Updates

Need extra days to review

Low designer entries

Target Market(s)

Niche

Font styles to use
Sans Serif

Requirements
Must have
• Fabric, Brightness, Nature
Nice to have
• Good colors
Should not have
• Adults

```html
<!DOCTYPE html>
<html lang="en">
<head>
<meta charset="utf-8">
<title>Softara Fabric Conditioner – Label</title>
<link rel="stylesheet" href="https://fonts.googleapis.com/css2?family=Roboto:wght@400;500;700;900&family=Great+Vibes&display=swap">
<style>
  :root {
    --bg: #ffffff;
    --navy: #13348f;
    --pink: #f54d8f;
    --white: #ffffff;
    --sky-top: #6fb8e0;
    --aqua-mid: #2ed3e0;
    --aqua-low: #63e6ec;
    --petal: #f4f9fa;
    --petal-shade: #c9eff3;
  }
  * { margin: 0; padding: 0; box-sizing: border-box; }
  html, body {
    width: 1200px;
    height: 1200px;
    overflow: hidden;
    background: var(--bg);
  }
  .canvas {
    position: relative;
    width: 1200px;
    height: 1200px;
    background: var(--bg);
  }
  .label {
    position: absolute;
    left: 250px;
    top: 80px;
    width: 700px;
    height: 1040px;
  }
  .label-shape {
    position: absolute;
    inset: 0;
    width: 700px;
    height: 1040px;
  }
  .tab-text {
    position: absolute;
    left: 205px;
    top: 112px;
    width: 300px;
    font-family: "Roboto", sans-serif;
    font-weight: 500;
    font-size: 26px;
    line-height: 1.1;
    color: var(--white);
    transform: rotate(-4deg);
    transform-origin: left top;
  }
  .brand-name {
    position: absolute;
    left: 80px;
    top: 360px;
    width: 560px;
    text-align: center;
    font-family: "Roboto", sans-serif;
    font-weight: 900;
    font-size: 118px;
    color: var(--navy);
    transform: rotate(-12deg);
  }
  .product-type {
    position: absolute;
    left: 150px;
    top: 545px;
    width: 420px;
    text-align: center;
    font-family: "Roboto", sans-serif;
    font-weight: 700;
    font-size: 25px;
    letter-spacing: 0.5px;
    color: var(--navy);
    transform: rotate(-12deg);
  }
  .tagline {
    position: absolute;
    left: 160px;
    top: 595px;
    width: 420px;
    text-align: center;
    font-family: "Great Vibes", cursive;
    font-size: 62px;
    line-height: 0.95;
    color: var(--navy);
    transform: rotate(-20deg);
  }
  .freshness-badge {
    position: absolute;
    left: 495px;
    top: 760px;
    width: 195px;
    height: 70px;
    background: var(--pink);
    border-radius: 14px 0 0 14px;
    display: flex;
    align-items: center;
    gap: 8px;
    padding-left: 14px;
    color: var(--white);
    font-family: "Roboto", sans-serif;
    font-weight: 700;
  }
  .freshness-badge .days-count { font-size: 48px; line-height: 1; }
  .freshness-badge .days-text { font-size: 16px; line-height: 1.05; }
  .loads {
    position: absolute;
    left: 510px;
    top: 842px;
    font-family: "Roboto", sans-serif;
    font-weight: 700;
    font-size: 28px;
    color: var(--navy);
  }
</style>
</head>
<body>
<div class="canvas">
  <div class="label">
    <svg class="label-shape" viewBox="0 0 700 1040" xmlns="http://www.w3.org/2000/svg">
      <defs>
        <linearGradient id="labelFill" x1="0" y1="0" x2="0" y2="1">
          <stop offset="0" stop-color="var(--sky-top)"/>
          <stop offset="0.55" stop-color="var(--aqua-mid)"/>
          <stop offset="1" stop-color="var(--aqua-low)"/>
        </linearGradient>
        <radialGradient id="flowerFill" cx="0.5" cy="0.45" r="0.7">
          <stop offset="0" stop-color="var(--petal)"/>
          <stop offset="0.6" stop-color="var(--petal-shade)"/>
          <stop offset="1" stop-color="var(--petal)"/>
        </radialGradient>
        <clipPath id="labelClip">
          <path d="M120 130 C260 40 560 60 640 260 L690 780 C700 940 560 1030 360 1030 C160 1030 20 940 20 760 L40 300 C50 210 80 160 120 130 Z"/>
        </clipPath>
        <path id="bottomArc" d="M140 900 C230 1010 490 1010 580 900"/>
      </defs>
      <path class="label-body" fill="url(#labelFill)" d="M120 130 C260 40 560 60 640 260 L690 780 C700 940 560 1030 360 1030 C160 1030 20 940 20 760 L40 300 C50 210 80 160 120 130 Z"/>
      <g clip-path="url(#labelClip)">
        <path class="pink-tab" fill="var(--pink)" d="M60 30 L600 30 C600 170 520 215 400 220 C280 225 170 235 40 300 Z"/>
        <g role="img" aria-label="Cluster of white jasmine flowers along the bottom of the label">
          <path fill="url(#flowerFill)" d="M20 780 C140 730 300 790 460 750 C560 725 640 735 700 750 L700 1040 L0 1040 Z"/>
        </g>
      </g>
      <text font-family="Roboto, sans-serif" font-weight="700" font-size="28" fill="var(--navy)">
        <textPath href="#bottomArc" startOffset="50%" text-anchor="middle">130 FL OZ (1.05 GAL) 3.99L</textPath>
      </text>
    </svg>

    <p class="tab-text">More Softening<br>ingredients</p>
    <h1 class="brand-name">Softara</h1>
    <p class="product-type">FABRIC CONDITIONER</p>
    <p class="tagline">Amazing Shine<br>&amp; Fragrance</p>

    <div class="freshness-badge">
      <span class="days-count">30</span>
      <span class="days-text">DAYS OF<br>FRESHNESS</span>
    </div>
    <p class="loads">120 LOADS</p>
  </div>
</div>
</body>
</html>
```